Bramford Holloway Inc. needs an innovative idea for letterhead and visiting cards.

Bramford Holloway Inc. is a Canadian brand since 2007. It is a renown dealer of kids and office furniture locally. Moreover, exporting electric fixtures e.g. switches, LED's, down-lights etc. to Middle East and Africa. We have initiated a number of steps including re-branding, to boost our export in 2020. We have successfully designed our new logo a few months ago through 'Mockplanet' and now we are looking for an innovative idea for a letterhead.
Some key points:
• Red, black and white are the three colors used in all our packaging and furniture. (grey is optional)
• Shouldn’t be too wide.
• Use of watermark is preferable.
• You can visit our North American site at www.bramfordhollowayinc.com. Export website of the company will be launched soon. www.bramfordhollowayinc.ca
• Same letterhead will be used locally and internationally.
• Our new logo and sample packaging is attached.

```html
<!DOCTYPE html>
<html lang="en">
<head>
<meta charset="utf-8">
<title>Bramford Holloway Inc. – Business Card</title>
<link rel="stylesheet" href="https://fonts.googleapis.com/css2?family=Questrial&family=Tinos:ital@0;1&display=swap">
<style>
  :root {
    --brand-red: #9c0a0f;
    --brand-grey: #4a4b4d;
    --paper-white: #ffffff;
    --stage: #ecebea;
  }
  * { margin: 0; padding: 0; box-sizing: border-box; }
  html, body { width: 1200px; height: 1106px; overflow: hidden; }
  body {
    position: relative;
    background: var(--stage);
    font-family: "Questrial", "Helvetica Neue", Arial, sans-serif;
    color: var(--paper-white);
  }
  .card {
    position: absolute;
    border-radius: 18px;
    overflow: hidden;
  }
  /* Front side */
  .card-front {
    left: 96px; top: 132px; width: 652px; height: 402px;
    background: var(--brand-grey);
  }
  .front-red-panel {
    position: absolute; left: 0; top: 0; width: 459px; height: 100%;
    background: var(--brand-red);
  }
  .front-divider {
    position: absolute; left: 456px; top: 0; width: 4px; height: 100%;
    background: var(--paper-white);
  }
  .holder-name {
    position: absolute; left: 30px; top: 56px;
    font-size: 23px; font-weight: 700; letter-spacing: 0.5px;
    font-family: "Questrial", Arial, sans-serif;
    -webkit-text-stroke: 0.6px var(--paper-white);
  }
  .holder-title {
    position: absolute; left: 31px; top: 83px; font-size: 17px;
  }
  .contact-list {
    position: absolute; left: 37px; top: 211px; list-style: none;
  }
  .contact-list li {
    display: flex; align-items: center; height: 24px; font-size: 17px;
  }
  .contact-list svg { width: 14px; height: 14px; margin-right: 8px; flex: none; }
  .postal-address {
    position: absolute; left: 40px; top: 312px; font-size: 17px; line-height: 24px;
    font-style: normal;
  }
  /* Back side */
  .card-back {
    left: 426px; top: 580px; width: 648px; height: 400px;
    background: var(--brand-grey);
  }
  .brand-lockup {
    position: absolute; left: 102px; top: 112px;
    display: flex; align-items: center;
  }
  .brand-square {
    width: 120px; height: 120px; background: var(--brand-red);
    border-radius: 10px; margin-right: 22px;
  }
  .brand-name {
    font-size: 52px; line-height: 60px; letter-spacing: 1px; color: var(--paper-white);
  }
  .brand-tagline {
    position: absolute; left: 296px; top: 232px;
    font-family: "Tinos", "Times New Roman", serif; font-size: 16px;
    color: var(--paper-white);
  }
  .brand-web {
    position: absolute; left: 0; width: 100%; top: 336px; text-align: center;
    font-size: 20px; letter-spacing: 2.4px;
  }
</style>
</head>
<body>
  <section class="card card-front" aria-label="Business card front">
    <div class="front-red-panel"></div>
    <div class="front-divider"></div>
    <h1 class="holder-name">CORIN ALDBURY</h1>
    <p class="holder-title">Managing Director</p>
    <ul class="contact-list">
      <li>
        <svg viewBox="0 0 14 14" aria-hidden="true"><path fill="#fff" d="M1 4c0-2 2-3 6-3s6 1 6 3v1h-3V4H4v1H1zM3 6h8l2 6H1z"/><circle cx="7" cy="9" r="1.6" fill="#9c0a0f"/></svg>
        044-615 2038 447
      </li>
      <li>
        <svg viewBox="0 0 14 14" aria-hidden="true"><rect x="1" y="3" width="12" height="8" fill="#fff"/><path d="M1 3l6 5 6-5" fill="none" stroke="#9c0a0f" stroke-width="1.2"/></svg>
        info@bramfordco.com
      </li>
      <li>
        <svg viewBox="0 0 14 14" aria-hidden="true"><circle cx="7" cy="7" r="6" fill="#fff"/><path d="M4 4c2 0 2 2 4 2s1 3 3 3M5 10c1-1 2 0 2 2" fill="none" stroke="#9c0a0f" stroke-width="1.2"/></svg>
        www.bramfordco.com
      </li>
    </ul>
    <address class="postal-address">No.123. Line Here<br>Address Country Name Here</address>
  </section>

  <section class="card card-back" aria-label="Business card back">
    <div class="brand-lockup">
      <div class="brand-square"></div>
      <div class="brand-name">BRAMFORD<br>HOLLOWAY</div>
    </div>
    <p class="brand-tagline">Because <i>You</i> Deserve The <i>Best</i></p>
    <p class="brand-web">www.bramfordholloway.ca</p>
  </section>
</body>
</html>
```